Builders Worksite Corflute Outdoor Sign

We are a building company who are just branching out into new construction. How first new build is our own home which was designed by us and a local architect. We are proud and want to create more advertisement around our business.

We need a corflute sign that can staked outside the construction site and can be seen by people passing by.
Updates

Can we please make the company name and logo bigger (Tidewater Lane Homes) This needs to be the focus. Can we please replace 'Mako' with 'Contact Us on 021-649-3157'

Target Market(s)

Home owners and people wishing to build on lifestyle blocks in New Zealand.

Font styles to use
Sans Serif

Requirements
Must have
• It needs to feature our:
Logo
Company name
Contact name and number - Mako - 0216493157
Landscape NOT portrait.

```html
<!DOCTYPE html>
<html lang="en">
<head>
<meta charset="utf-8">
<title>Tidewater Lane Homes – Site Sign</title>
<link rel="stylesheet" href="https://fonts.googleapis.com/css2?family=Jost:wght@400&family=Poppins:wght@700;800&display=swap">
<style>
  :root {
    --navy: #1b2747;
    --gold: #f8c70f;
    --gold-deep: #d9a21c;
    --panel: #f4f4f5;
    --backdrop: #e6e7ea;
  }
  * { box-sizing: border-box; margin: 0; padding: 0; }
  html, body {
    width: 771px;
    height: 1200px;
    overflow: hidden;
    background: var(--backdrop);
  }
  .sign {
    position: absolute;
    left: 36px;
    top: 320px;
    width: 700px;
    height: 560px;
    background: var(--panel);
    box-shadow: 0 6px 18px rgba(0,0,0,0.18);
  }
  .sign__field {
    position: absolute;
    inset: 0 0 150px 0;
    background: var(--panel);
  }
  .brand {
    position: absolute;
    top: 34px;
    left: 0;
    right: 0;
    text-align: center;
    font-family: "Jost", sans-serif;
    font-weight: 400;
    color: var(--navy);
  }
  .brand__dot {
    display: block;
    width: 96px;
    height: 96px;
    margin: 0 auto 26px;
    border-radius: 50%;
    background: var(--gold);
  }
  .brand__name {
    display: block;
    font-size: 66px;
    line-height: 1;
    letter-spacing: 0.01em;
  }
  .brand__sub {
    display: block;
    margin-top: 22px;
    font-size: 44px;
    line-height: 1;
    letter-spacing: 0.45em;
    padding-left: 0.45em;
  }
  .sign__rule {
    position: absolute;
    left: 0;
    right: 0;
    top: 406px;
    height: 4px;
    background: var(--gold);
  }
  .sign__band {
    position: absolute;
    left: 0;
    right: 0;
    bottom: 0;
    height: 150px;
    background: var(--navy);
  }
  .contact-pill {
    position: absolute;
    left: 50%;
    top: 386px;
    transform: translateX(-50%);
    width: 262px;
    height: 46px;
    border-radius: 23px;
    background: var(--gold);
    color: var(--navy);
    font-family: "Poppins", sans-serif;
    font-weight: 700;
    font-size: 27px;
    line-height: 46px;
    text-align: center;
  }
  .phone {
    position: absolute;
    left: 0;
    right: 0;
    bottom: 18px;
    text-align: center;
    font-family: "Poppins", sans-serif;
    font-weight: 800;
    font-size: 92px;
    line-height: 1;
    letter-spacing: 0.01em;
    color: var(--gold);
    text-shadow: 2px 2px 0 #0d142a;
  }
</style>
</head>
<body>
  <div class="sign">
    <div class="sign__field" role="img" aria-label="Light grey decorative background pattern"></div>
    <div class="brand">
      <span class="brand__dot"></span>
      <span class="brand__name">TIDEWATER LANE</span>
      <span class="brand__sub">HOMES</span>
    </div>
    <div class="sign__rule"></div>
    <div class="sign__band">
      <div class="phone">0216493157</div>
    </div>
    <div class="contact-pill">Contact Us</div>
  </div>
</body>
</html>
```